Website for Party

Design a new website for PrismGatherings.com
We have attached the new logos and please look at the website, and our facebook page: facebook.com/prismgatherings for inspiration
Updates

Hi Guys, please be original with all designs and images otherwise the design will be eliminated Thank you

some of your designs have too much happening in them, others make it clear that the designer has not yet read the brief fully

Please everyone be original!

```html
<!DOCTYPE html>
<html lang="en">
<head>
<meta charset="utf-8">
<title>Prism Gatherings</title>
<link href="https://fonts.googleapis.com/css2?family=Open+Sans:ital,wght@0,300;0,400;0,600;1,400&family=Silkscreen:wght@400;700&display=swap" rel="stylesheet">
<style>
:root{
  --black:#000;
  --white:#fff;
  --yellow:#ffe500;
  --blue:#0a6ee8;
  --nav-blue:#1d5fb0;
  --nav-blue-dark:#0f4a93;
  --green:#33ff00;
  --orange:#ff8a3d;
  --grey-text:#333;
  --rule:#dcdcdc;
  --panel:#e6e6e6;
  --icon-grey:#8c8c8c;
}
*{margin:0;padding:0;box-sizing:border-box}
html,body{width:1200px;height:1095px;overflow:hidden;background:var(--white)}
body{font-family:"Open Sans",Arial,sans-serif;color:var(--grey-text);position:relative}
.abs{position:absolute}

.site-header{left:0;top:0;width:1200px;height:100px;background:var(--black)}
.brand{left:230px;top:10px;width:80px;text-align:center;color:var(--white)}
.brand-mark{display:block;font-size:40px;font-weight:600;line-height:52px}
.brand-name{display:block;font-size:12px;font-weight:600;letter-spacing:3px;margin-top:12px}
.social{left:451px;top:60px;display:flex;gap:3px}
.social span{width:20px;height:20px;border-radius:50%;background:var(--icon-grey)}
.help{right:232px;top:16px;text-align:right;color:var(--white);font-size:13px;line-height:20px}
.help-title{color:var(--yellow);font-size:20px;font-weight:300;line-height:26px;margin-bottom:4px}

.main-nav{left:0;top:100px;width:1200px;height:28px;background:linear-gradient(to bottom,var(--nav-blue),var(--nav-blue-dark));border-bottom:1px solid var(--yellow)}
.main-nav ul{list-style:none;display:flex;position:absolute;right:232px;top:5px;gap:0}
.main-nav li{color:var(--white);font-size:13px;margin-left:40px}

.hero{left:0;top:128px;width:1200px;height:403px;background:#0a0f2a;overflow:hidden}
.hero-photo{left:95px;top:0;width:1105px;height:403px;background:radial-gradient(ellipse at 30% 20%,#b86a3a 0%,#5a3a3a 25%,#23335c 55%,#0c1430 85%)}
.headline{left:231px;top:120px;font-weight:300;font-size:44px;line-height:48px;color:#111}
.headline .line{display:inline-block;background:var(--white);padding:0 10px 0 17px}
.headline .line2{padding-left:13px}
.headline .now{background:var(--green);color:var(--white);padding:0 12px;margin-left:-2px;font-weight:400}
.banner{left:220px;top:474px;width:758px;height:72px}
.banner-text{left:236px;top:487px;width:728px;height:46px;text-align:center;color:var(--white);font-family:"Silkscreen",monospace;font-size:28px;line-height:46px}
.slider-dots{left:531px;top:548px;display:flex;gap:4px}
.slider-dots span{width:24px;height:4px;background:#aaa}
.slider-dots .active{background:var(--black)}

.tagline{left:0;top:580px;width:1200px;text-align:center;font-size:20px;font-weight:300;color:#444}
.tagline b{font-weight:400;letter-spacing:4px;color:#111}
.rule{left:230px;width:740px;height:1px;background:linear-gradient(to right,transparent,var(--rule) 20%,var(--rule) 80%,transparent)}
.section-title{left:0;width:1200px;text-align:center;font-size:26px;font-weight:300;color:#111}

.arrow{top:715px;width:12px;height:70px;background:var(--yellow)}
.arrow svg{position:absolute;left:3px;top:31px}
.event{top:697px;width:149px}
.event-photo{width:149px;height:64px}
.event-title{font-size:13px;line-height:17px;margin-top:6px;height:44px;color:#222}
.book{display:inline-block;background:var(--green);color:#111;font-size:13px;line-height:25px;padding:0 12px;margin-top:8px}

.query{left:230px;top:927px;width:738px;height:65px;background:var(--panel)}
.field{top:23px;height:19px;background:var(--white);border:1px solid #999;font-size:10px;font-style:italic;color:#888;padding-left:7px;line-height:17px}
.submit{left:665px;top:24px;width:62px;height:18px;background:var(--orange);color:var(--white);font-size:10px;text-align:center;line-height:18px}

.site-footer{left:0;top:1040px;width:1200px;height:55px;background:var(--black);overflow:hidden}
.copyright{left:232px;top:13px;font-size:10px;font-style:italic;color:var(--white)}
</style>
</head>
<body>

<header class="site-header abs">
  <div class="brand abs">
    <span class="brand-mark">Prism</span>
  </div>
  <div class="social abs" aria-label="Social links">
    <span></span><span></span><span></span><span></span><span></span><span></span><span></span>
  </div>
  <div class="help abs">
    <div class="help-title">Let us Help you</div>
    <div>Dial: 1800-555-010-0199</div>
    <div>Email: enquiries@prismgatherings.com</div>
  </div>
</header>

<nav class="main-nav abs">
  <ul>
    <li>Home</li><li>About Us</li><li>FAQ</li><li>Order Tickets</li><li>Contact Us</li>
  </ul>
</nav>

<section class="hero abs">
  <div class="hero-photo abs" role="img" aria-label="Blurred photo of a DJ's hands on a turntable"></div>
  <h1 class="headline abs">
    <span class="line">Order Tickets</span><br>
    <span class="line line2">Online <span class="now">NOW!</span></span>
  </h1>
</section>

<svg class="banner abs" viewBox="0 0 758 72" aria-hidden="true">
  <polygon points="10,2 748,2 748,50 758,72 2,72 0,40" fill="var(--yellow)"/>
  <polygon points="10,2 748,2 756,62 16,70" fill="var(--blue)"/>
  <polygon points="10,2 400,2 30,70 2,70 0,40" fill="var(--yellow)"/>
  <rect x="16" y="13" width="728" height="46" fill="var(--black)"/>
</svg>
<div class="banner-text abs">Exclusive VIP July 4th Party</div>
<div class="slider-dots abs"><span class="active"></span><span></span><span></span><span></span><span></span></div>

<p class="tagline abs"><b>Prism</b> = Talented Artists | Spectacular Venues</p>
<div class="rule abs" style="top:625px"></div>

<h2 class="section-title abs" style="top:645px">Events Lined up</h2>

<div class="arrow abs" style="left:226px"><svg width="6" height="8"><polygon points="6,0 6,8 0,4" fill="#000"/></svg></div>
<div class="arrow abs" style="left:961px"><svg width="6" height="8"><polygon points="0,0 6,4 0,8" fill="#000"/></svg></div>

<article class="event abs" style="left:259px">
  <div class="event-photo" role="img" aria-label="Harbour skyline at sunset" style="background:linear-gradient(to bottom,#5a7aa8,#c9a78a 55%,#2c3a55 75%,#3c5e8a)"></div>
  <p class="event-title">&nbsp;3+ Hour Cruise around<br>&nbsp;NYC Harbor</p>
  <span class="book">BOOK TICKETS</span>
</article>
<article class="event abs" style="left:440px">
  <div class="event-photo" role="img" aria-label="Lemon slices with mint and ice" style="background:linear-gradient(135deg,#dfe6c8,#e8e23a 40%,#f1f1ea 70%,#c8d0d0)"></div>
  <p class="event-title">&nbsp;Open Premium Bar</p>
  <span class="book">BOOK TICKETS</span>
</article>
<article class="event abs" style="left:621px">
  <div class="event-photo" role="img" aria-label="Plate of hors d'oeuvres" style="background:linear-gradient(90deg,#e7c99a,#d9a874 45%,#8a3a2a 65%,#e9c59a)"></div>
  <p class="event-title">Hors d'oeuvres</p>
  <span class="book">BOOK TICKETS</span>
</article>
<article class="event abs" style="left:793px">
  <div class="event-photo" role="img" aria-label="Singer performing on stage" style="background:linear-gradient(90deg,#5a1a6a,#3a1a40 40%,#151018)"></div>
  <p class="event-title">Opening Performance<br>by Eli Marlow</p>
  <span class="book">BOOK TICKETS</span>
</article>

<div class="rule abs" style="top:858px"></div>
<h2 class="section-title abs" style="top:877px">Quick Query</h2>

<form class="query abs">
  <div class="field abs" style="left:10px;width:191px">Name</div>
  <div class="field abs" style="left:215px;width:191px">Email</div>
  <div class="field abs" style="left:418px;width:234px">Message</div>
  <div class="submit abs">SUBMIT</div>
</form>

<footer class="site-footer abs">
  <p class="copyright abs">Copyright © Prism. All rights reserved.</p>
  <svg class="abs" style="left:226px;top:36px" width="750" height="19" aria-hidden="true">
    <polygon points="20,0 745,0 750,19 0,19" fill="var(--blue)"/>
    <polygon points="20,0 120,0 400,19 0,19" fill="var(--yellow)"/>
    <polygon points="120,2 745,0 745,4 300,19 200,19" fill="var(--blue)"/>
  </svg>
</footer>

</body>
</html>
```